Business Card Design Project

Business card based on attached logo

Tom Pellis
Tom@vorlatests.example
555-014-7731 ext. 219
Www.VorlaTests.example

Industry/Entity Type

Business

```html
<!DOCTYPE html>
<html lang="en">
<head>
<meta charset="utf-8">
<title>Vorla Tests Business Card</title>
<link rel="stylesheet" href="https://fonts.googleapis.com/css2?family=Arimo:ital,wght@0,400;0,700;1,400;1,700&display=swap">
<style>
  :root {
    --bg: #efeeec;
    --card: #ffffff;
    --ink: #1e1e1e;
    --band-dark: #232323;
    --band-dark-hi: #3a3a3a;
    --brand-red: #e0141c;
    --text-body: #222222;
  }
  * { box-sizing: border-box; margin: 0; padding: 0; }
  html, body {
    width: 1200px; height: 868px; overflow: hidden;
    background: var(--bg);
    font-family: "Arimo", Arial, sans-serif;
  }
  .canvas { position: relative; width: 1200px; height: 868px; }
  .card {
    position: absolute;
    width: 540px; height: 309px;
    background: var(--card);
    border-radius: 16px;
    overflow: hidden;
    box-shadow: 0 6px 18px rgba(0,0,0,.18);
  }
  .card--back { left: 40px; top: 280px; }
  .card--front { left: 620px; top: 280px; }

  .brand-name {
    color: var(--ink);
    font-weight: 700;
    text-transform: uppercase;
    line-height: 1;
  }
  .card--back .brand-name {
    position: absolute; left: 110px; top: 90px;
    font-size: 62px; letter-spacing: -1px;
  }
  .card--back .brand-name span { display: block; font-size: 40px; letter-spacing: 10px; margin-top: 8px; margin-left: 4px; }

  .band { position: absolute; left: 0; right: 0; bottom: 0; display: flex; }
  .card--back .band { height: 22px; }
  .band__dark { flex: 0 0 58%; background: linear-gradient(var(--band-dark-hi), var(--band-dark)); }
  .band__red { flex: 1; background: var(--brand-red); }

  .card--front .brand-name {
    position: absolute; left: 42px; top: 38px;
    font-size: 32px; letter-spacing: -0.5px;
  }
  .card--front .brand-name span { display: block; font-size: 20px; letter-spacing: 5px; margin-top: 4px; margin-left: 2px; }
  .logo-rule {
    position: absolute; left: 0; top: 112px; width: 268px; height: 3px;
    background: var(--brand-red);
    box-shadow: 0 2px 0 var(--band-dark);
  }
  .person-name {
    position: absolute; right: 40px; top: 92px;
    font-size: 27px; font-weight: 700; color: var(--ink);
  }
  .contact { position: absolute; left: 36px; top: 160px; list-style: none; }
  .contact li {
    display: flex; align-items: center; gap: 12px;
    font-size: 17px; font-style: italic; color: var(--text-body);
    margin-bottom: 7px;
  }
  .contact svg { width: 13px; height: 13px; fill: var(--ink); }

  .card--front .band { height: 60px; }
  .card--front .band__dark { flex: 0 0 72%; align-items: center; display: flex; padding-left: 40px; }
  .website { color: var(--brand-red); font-weight: 700; font-style: italic; font-size: 16px; }
  .badge {
    position: absolute; right: 70px; bottom: 20px;
    width: 96px; height: 96px; border-radius: 50%;
    background: radial-gradient(circle at 50% 35%, #ffffff, #e4e4e4);
    box-shadow: 0 3px 8px rgba(0,0,0,.3);
  }
</style>
</head>
<body>
<main class="canvas">
  <section class="card card--back" aria-label="Card back">
    <div class="brand-name">Vorla<span>Tests</span></div>
    <div class="band"><div class="band__dark"></div><div class="band__red"></div></div>
  </section>

  <section class="card card--front" aria-label="Card front">
    <div class="brand-name">Vorla<span>Tests</span></div>
    <div class="logo-rule"></div>
    <h1 class="person-name">Tom Pellis</h1>
    <ul class="contact">
      <li>
        <svg viewBox="0 0 16 12" aria-hidden="true"><path d="M0 0h16v12H0z M1.5 1.5 8 6.5l6.5-5" fill="none" stroke="#1e1e1e" stroke-width="2"/></svg>
        Tom@vorlatests.example
      </li>
      <li>
        <svg viewBox="0 0 16 16" aria-hidden="true"><path d="M3.5 1 6 4 4.6 5.8c.9 2.2 3.4 4.7 5.6 5.6L12 10l3 2.5-1.6 2.5C7.5 14.5 1.5 8.5 1 2.6z"/></svg>
        555-014-7731 ext. 219
      </li>
    </ul>
    <div class="band">
      <div class="band__dark"><span class="website">www.VorlaTests.example</span></div>
      <div class="band__red"></div>
    </div>
    <div class="badge"></div>
  </section>
</main>
</body>
</html>
```